Card Design for my dog training business Rustpaw Obedience

Need a business card design for my dog training business with my new logo. Want the card to come off professional yet fun. Want it to be very eye catchy as well. I normally have these at vet clinics, pet stores, and groomers. so need it to look better than my competitors.
Target Market(s)
dog owners
Industry/Entity Type
Dog Training
Contact Information for Business Card
needs logo, my name and info
Font styles to use
Serif
Colors
0255a3
ffffff
ec1f27
000000
333333
fbfbfb
Requirements
Must have
- Rustpaw Obedience
- Hollis Brandt
- 415 903 2267
- info@rustpawobedience.example
- www.rustpawobedience.example

```html
<!DOCTYPE html>
<html lang="en">
<head>
<meta charset="utf-8">
<title>Rustpaw Obedience – Business Card</title>
<link rel="stylesheet" href="https://fonts.googleapis.com/css2?family=Cormorant+Garamond:ital,wght@0,600;1,400&family=Montserrat:wght@400;600&display=swap">
<style>
  :root {
    --backdrop: #2a2a2a;
    --card: #111111;
    --card-edge: #1c1c1c;
    --silver: #e6e6e6;
    --silver-soft: #bdbdbd;
    --tagline-faint: #2f2f2f;
  }
  * { box-sizing: border-box; margin: 0; padding: 0; }
  html, body { width: 1200px; height: 716px; overflow: hidden; }
  body { background: var(--backdrop); position: relative; font-family: "Montserrat", sans-serif; }

  .card {
    position: absolute;
    width: 500px; height: 286px;
    background: var(--card);
    border: 1px solid var(--card-edge);
    border-radius: 18px;
    color: var(--silver);
  }
  .card--front { left: 70px; top: 80px; }
  .card--back { left: 630px; top: 340px; }

  .brand {
    font-family: "Cormorant Garamond", serif;
    font-weight: 600;
    color: var(--silver);
    letter-spacing: 1px;
    text-align: center;
    display: flex; flex-direction: column; align-items: center; gap: 10px;
  }
  .brand__dot { width: 14px; height: 14px; border-radius: 50%; background: var(--silver); }

  .card--front .brand { position: absolute; left: 0; right: 0; top: 80px; font-size: 38px; }
  .card--front .tagline {
    position: absolute; left: 0; right: 0; top: 190px;
    text-align: center;
    font-family: "Cormorant Garamond", serif; font-style: italic;
    font-size: 15px; color: var(--silver-soft);
  }

  .card--back .brand { position: absolute; left: 30px; width: 190px; top: 82px; font-size: 26px; line-height: 1.1; }
  .divider { position: absolute; left: 238px; top: 60px; width: 1px; height: 128px; background: var(--silver); }
  .contact { position: absolute; left: 262px; top: 70px; }
  .contact__name { font-weight: 600; font-size: 17px; letter-spacing: 0.5px; margin-bottom: 14px; }
  .contact__list { list-style: none; font-size: 11px; display: flex; flex-direction: column; gap: 9px; }
  .contact__item { display: flex; align-items: center; gap: 9px; }
  .contact__icon { width: 11px; height: 11px; fill: var(--silver); flex: none; }
  .card--back .tagline {
    position: absolute; left: 0; right: 0; bottom: 40px; text-align: center;
    font-family: "Cormorant Garamond", serif; font-style: italic;
    font-size: 21px; color: var(--tagline-faint);
  }
</style>
</head>
<body>
  <section class="card card--front">
    <div class="brand"><span class="brand__dot"></span>Rustpaw Obedience</div>
    <p class="tagline">“Training dogs across Texas one dog at a time.”</p>
  </section>

  <section class="card card--back">
    <div class="brand"><span class="brand__dot"></span>Rustpaw Obedience</div>
    <div class="divider"></div>
    <div class="contact">
      <p class="contact__name">HOLLIS BRANDT</p>
      <ul class="contact__list">
        <li class="contact__item">
          <svg class="contact__icon" viewBox="0 0 24 24" aria-hidden="true"><path d="M6.6 10.8a15 15 0 0 0 6.6 6.6l2.2-2.2a1 1 0 0 1 1-.25 11.4 11.4 0 0 0 3.6.57 1 1 0 0 1 1 1V20a1 1 0 0 1-1 1A17 17 0 0 1 3 4a1 1 0 0 1 1-1h3.5a1 1 0 0 1 1 1c0 1.25.2 2.45.57 3.6a1 1 0 0 1-.25 1z"/></svg>
          415 903 2267
        </li>
        <li class="contact__item">
          <svg class="contact__icon" viewBox="0 0 24 24" aria-hidden="true"><path d="M2 5h20v14H2z M3.5 6.5 12 13l8.5-6.5" fill="none" stroke="#e6e6e6" stroke-width="2"/><path d="M2 5h20L12 12z"/></svg>
          info@rustpawobedience.example
        </li>
        <li class="contact__item">
          <svg class="contact__icon" viewBox="0 0 24 24" aria-hidden="true"><g fill="none" stroke="#e6e6e6" stroke-width="2"><circle cx="12" cy="12" r="10"/><ellipse cx="12" cy="12" rx="4" ry="10"/><path d="M2 12h20"/></g></svg>
          www.rustpawobedience.example
        </li>
      </ul>
    </div>
    <p class="tagline">“Training dogs across Texas one dog at a time.”</p>
  </section>
</body>
</html>
```